Simple and clean

We need a business card design for a new company called Estate Lantern. It is a search engine to find current properties for sale or rent in New Zealand market.
We have already a colour scheme that we would like people to use.
Light brown: #D4CCB0
Light green: #D6E4D4
Green: #669966
Black/White
It is OK to divert from this colour scheme slightly as long as there is a green component to the business card.
Final design should be clean, simple and should communicate the nature of the business.
Target Market(s)
- First home buyers
- Real estate agents
- People seeking rentals
Industry/Entity Type
Business
Requirements
Must have
- Use those or similar colours.
Light brown: #D4CCB0
Light green: #D6E4D4
Green: #669966
Black/White

```html
<!DOCTYPE html>
<html lang="en">
<head>
<meta charset="utf-8">
<title>Estate Lantern – Business Card</title>
<link rel="stylesheet" href="https://fonts.googleapis.com/css2?family=Open+Sans:wght@600;700&family=Arimo:wght@400&display=swap">
<style>
  :root {
    --page-bg: #ffffff;
    --card-black: #000000;
    --brand-green: #669966;
    --logo-light: #d6e4d4;
    --accent-bright: #46e84c;
    --text-white: #ffffff;
    --shadow: rgba(0, 0, 0, 0.35);
  }
  * { box-sizing: border-box; margin: 0; padding: 0; }
  html, body {
    width: 1200px;
    height: 900px;
    overflow: hidden;
    background: var(--page-bg);
  }
  .business-card {
    position: absolute;
    left: 180px;
    top: 180px;
    width: 840px;
    height: 540px;
    background: var(--card-black);
    box-shadow: 0 6px 18px var(--shadow);
    overflow: hidden;
  }
  .brand {
    position: absolute;
    left: 48px;
    top: 208px;
    display: flex;
    align-items: center;
    gap: 14px;
  }
  .brand-dot {
    width: 26px;
    height: 26px;
    border-radius: 50%;
    background: var(--brand-green);
  }
  .brand-name {
    font-family: "Open Sans", sans-serif;
    font-weight: 600;
    font-size: 42px;
    color: var(--logo-light);
    letter-spacing: -0.5px;
    white-space: nowrap;
  }
  .divider {
    position: absolute;
    left: 452px;
    top: 30px;
    width: 3px;
    height: 370px;
    background: linear-gradient(to bottom,
      rgba(70, 232, 76, 0) 0%,
      var(--accent-bright) 55%,
      rgba(70, 232, 76, 0) 100%);
  }
  .contact {
    position: absolute;
    left: 488px;
    top: 56px;
  }
  .contact-name {
    font-family: "Open Sans", sans-serif;
    font-weight: 700;
    font-size: 31px;
    line-height: 1;
    color: var(--brand-green);
    white-space: nowrap;
  }
  .contact-role {
    font-family: "Open Sans", sans-serif;
    font-weight: 700;
    font-size: 23px;
    line-height: 1.1;
    color: var(--brand-green);
    margin-top: 2px;
  }
  .contact-details {
    margin-top: 42px;
    font-family: "Arimo", sans-serif;
    font-size: 21px;
    line-height: 1.1;
    color: var(--text-white);
    list-style: none;
  }
  .contact-web {
    margin-top: 30px;
    font-family: "Arimo", sans-serif;
    font-size: 21px;
    color: var(--text-white);
    white-space: nowrap;
  }
  .footer-band {
    position: absolute;
    left: 0;
    bottom: 0;
    width: 100%;
    height: 76px;
    background: var(--accent-bright);
    display: flex;
    justify-content: center;
    padding-top: 12px;
  }
  .footer-web {
    font-family: "Open Sans", sans-serif;
    font-weight: 700;
    font-size: 20px;
    letter-spacing: 5px;
    color: var(--card-black);
    white-space: nowrap;
  }
</style>
</head>
<body>
  <article class="business-card">
    <div class="brand">
      <span class="brand-dot"></span>
      <span class="brand-name">Estate Lantern</span>
    </div>
    <div class="divider"></div>
    <section class="contact">
      <h1 class="contact-name">Tessa Varnell</h1>
      <h2 class="contact-role">Director</h2>
      <ul class="contact-details">
        <li>Mobile number</li>
        <li>Email address</li>
      </ul>
      <p class="contact-web">www.estatelantern.co.nz</p>
    </section>
    <footer class="footer-band">
      <span class="footer-web">www.estatelantern.co.nz</span>
    </footer>
  </article>
</body>
</html>
```